Financial Planning firm focused on serving women 55-65 yrs old needs stationary design

We are rebranding our financial planning firm and our target client is a 55-65 yr old women. We need a stationary design to go with our new logo.

Contact Information: Raymond Kessler, MS, CFP President Harlow Wealth Management 4820 Bramblewood Lane, Suite 317 Estero, FL 33961 ray@harlowwealthmgmt.example phone 239-555-0184

```html
<!DOCTYPE html>
<html lang="en">
<head>
<meta charset="utf-8">
<title>Harlow Wealth Management – Stationery</title>
<link rel="stylesheet" href="https://fonts.googleapis.com/css2?family=Oswald:wght@500&family=Source+Sans+3:wght@400;600&display=swap">
<style>
  :root {
    --blue: #2d6389;
    --green: #1f6b3a;
    --sage: #a7b8a6;
    --sage-faint: #dbe1da;
    --paper: #ffffff;
    --ink: #333333;
    --backdrop: #ebe8e3;
    --edge: #55606a;
  }
  * { box-sizing: border-box; margin: 0; padding: 0; }
  html, body { width: 1200px; height: 695px; overflow: hidden; }
  body {
    position: relative;
    background: var(--backdrop);
    font-family: "Source Sans 3", Arial, sans-serif;
    color: var(--ink);
  }
  .sheet { position: absolute; background: var(--paper); overflow: hidden; }
  .bordered { border: 1px solid var(--edge); }

  /* Brand lockup: plain circle + name in one colour and weight */
  .brand { position: absolute; display: flex; align-items: center; gap: 7px; }
  .brand-mark { border-radius: 50%; background: var(--sage); flex: none; }
  .brand-name {
    font-family: "Oswald", Arial, sans-serif;
    font-weight: 500;
    color: var(--blue);
    line-height: 1;
    text-transform: uppercase;
  }
  .brand-name .line-main { display: block; letter-spacing: 1px; }
  .brand-name .line-sub { display: block; letter-spacing: 0.5px; margin-top: 3px; }

  .footer-band {
    position: absolute; left: 0; right: 0; bottom: 0;
    background: var(--blue);
    color: #fff;
    display: flex; align-items: center; justify-content: center;
  }
  .footer-rule { position: absolute; left: 0; right: 0; height: 2px; background: var(--green); }

  .contact-list { position: absolute; font-size: 8px; line-height: 13px; }
  .contact-list li { list-style: none; display: flex; align-items: center; gap: 3px; }
  .contact-list svg { width: 7px; height: 7px; fill: var(--blue); }

  /* Letterhead */
  .letterhead { left: 22px; top: 31px; width: 498px; height: 642px; border: 1px solid #c9c9c9; }
  .letterhead .brand { left: 11px; top: 12px; }
  .letterhead .brand-mark { width: 52px; height: 52px; }
  .letterhead .line-main { font-size: 32px; }
  .letterhead .line-sub { font-size: 8px; }
  .letterhead .contact-list { right: 16px; top: 31px; padding-left: 4px; border-left: 1px solid var(--blue); }
  .letterhead .watermark {
    position: absolute; left: 140px; top: 210px; width: 220px; height: 220px;
    border-radius: 50%; background: var(--sage-faint);
  }
  .letterhead .footer-rule { bottom: 33px; }
  .letterhead .footer-band { height: 31px; font-size: 10px; letter-spacing: 0.3px; }

  /* Envelopes */
  .envelope-back { left: 616px; top: 38px; width: 557px; height: 240px; }
  .envelope-open { left: 578px; top: 147px; width: 557px; height: 200px; }
  .envelope-back svg, .envelope-open svg { position: absolute; inset: 0; }

  .envelope-front { left: 537px; top: 253px; width: 557px; height: 241px; }
  .envelope-front .brand { left: 10px; top: 13px; }
  .envelope-front .brand-mark { width: 46px; height: 46px; }
  .envelope-front .line-main { font-size: 29px; }
  .envelope-front .line-sub { font-size: 7px; }
  .envelope-front .footer-rule { bottom: 33px; }
  .envelope-front .footer-band { height: 30px; font-size: 11px; letter-spacing: 1.5px; }

  /* Business card */
  .card-front { left: 573px; top: 513px; width: 274px; height: 155px; }
  .card-front .brand { left: 70px; top: 15px; }
  .card-front .brand-mark { width: 46px; height: 46px; }
  .card-front .line-main { font-size: 29px; }
  .card-front .line-sub { font-size: 7px; }
  .card-front .address {
    position: absolute; right: 141px; top: 87px; text-align: right;
    font-size: 7px; line-height: 13px; font-style: normal;
  }
  .card-front .contact-list { left: 139px; top: 86px; font-size: 7px; padding-left: 4px; border-left: 1px solid var(--blue); }
  .card-front .footer-rule { bottom: 20px; height: 1.5px; }
  .card-front .footer-band { height: 18px; font-size: 9px; font-weight: 600; gap: 3px; }
  .card-front .credentials { font-size: 6px; font-weight: 400; }

  .card-back { left: 852px; top: 513px; width: 274px; height: 155px; background: var(--blue); color: #fff; }
  .card-back .brand-mark { position: absolute; left: 96px; top: 26px; width: 94px; height: 94px; }
  .card-back .web { position: absolute; left: 0; right: 0; top: 131px; text-align: center; font-size: 9px; letter-spacing: 1px; }
</style>
</head>
<body>

<!-- Envelope, flap open, back view -->
<div class="sheet bordered envelope-back">
  <svg viewBox="0 0 557 240" width="557" height="240" aria-hidden="true">
    <polygon points="0,0 557,0 557,74 548,80 9,80 0,74" fill="var(--blue)"/>
    <circle cx="278" cy="38" r="24" fill="var(--sage)"/>
  </svg>
</div>

<!-- Envelope, flap open, inside view -->
<div class="sheet bordered envelope-open">
  <svg viewBox="0 0 557 200" width="557" height="200" aria-hidden="true">
    <polyline points="0,0 36,76 521,76 557,0" fill="none" stroke="var(--edge)" stroke-width="1"/>
    <circle cx="278" cy="38" r="24" fill="var(--sage)"/>
  </svg>
</div>

<!-- Envelope front -->
<div class="sheet bordered envelope-front">
  <div class="brand">
    <span class="brand-mark"></span>
    <span class="brand-name"><span class="line-main">Harlow</span><span class="line-sub">Wealth Management</span></span>
  </div>
  <div class="footer-rule"></div>
  <div class="footer-band">www.harlowwealthmgmt.example</div>
</div>

<!-- Letterhead -->
<div class="sheet letterhead">
  <div class="brand">
    <span class="brand-mark"></span>
    <span class="brand-name"><span class="line-main">Harlow</span><span class="line-sub">Wealth Management</span></span>
  </div>
  <ul class="contact-list">
    <li><svg viewBox="0 0 10 10"><path d="M2 0h2l1 3-1.5 1a6 6 0 0 0 2.5 2.5L7 5l3 1v2c0 1-1 2-2 2A8 8 0 0 1 0 2c0-1 1-2 2-2z"/></svg>239-555-0184</li>
    <li><svg viewBox="0 0 10 10"><path d="M0 2h10v6H0z M0 2l5 3.5L10 2" stroke="#fff" stroke-width="0.8"/></svg>ray@harlowwealthmgmt.example</li>
  </ul>
  <div class="watermark"></div>
  <div class="footer-rule"></div>
  <div class="footer-band">4820 Bramblewood Lane, Suite 317, Estero, FL&nbsp; 33961</div>
</div>

<!-- Business card front -->
<div class="sheet bordered card-front">
  <div class="brand">
    <span class="brand-mark"></span>
    <span class="brand-name"><span class="line-main">Harlow</span><span class="line-sub">Wealth Management</span></span>
  </div>
  <address class="address">4820 Bramblewood Lane, Suite 317<br>Estero, FL&nbsp; 33961</address>
  <ul class="contact-list">
    <li><svg viewBox="0 0 10 10"><path d="M2 0h2l1 3-1.5 1a6 6 0 0 0 2.5 2.5L7 5l3 1v2c0 1-1 2-2 2A8 8 0 0 1 0 2c0-1 1-2 2-2z"/></svg>239-555-0184</li>
    <li><svg viewBox="0 0 10 10"><path d="M0 2h10v6H0z M0 2l5 3.5L10 2" stroke="#fff" stroke-width="0.8"/></svg>ray@harlowwealthmgmt.example</li>
  </ul>
  <div class="footer-rule"></div>
  <div class="footer-band">Raymond Kessler <span class="credentials">MS, CFP</span> President</div>
</div>

<!-- Business card back -->
<div class="sheet card-back">
  <span class="brand-mark"></span>
  <div class="web">www.harlowwealthmgmt.example</div>
</div>

</body>
</html>
```